Restaurant, Nightclub

It's a Restaurant come nightclub. Our sign Lumen is white letters with blue edging on a black back ground.

Industry/Entity Type

Restaurant

Contact Information for Business Card

Lumen Stevenage Ltd
42 Mill Lane
Stevenage Herts SG2 7PQ

```html
<!DOCTYPE html>
<html lang="en">
<head>
<meta charset="utf-8">
<title>Lumen Stevenage – Business Card</title>
<link rel="stylesheet" href="https://fonts.googleapis.com/css2?family=Saira:wght@400;700&family=Arimo:wght@700&display=swap">
<style>
  :root {
    --card-black: #07070a;
    --photo-centre: #1a1a2e;
    --photo-mid: #100f16;
    --text-white: #ffffff;
    --text-soft: #e8eef2;
    --accent-cyan: #4fc3e0;
  }
  html, body {
    margin: 0;
    padding: 0;
    width: 1200px;
    height: 791px;
    overflow: hidden;
    background: var(--card-black);
  }
  .card {
    position: relative;
    width: 1200px;
    height: 791px;
    overflow: hidden;
    background: var(--card-black);
    font-family: "Saira", sans-serif;
    color: var(--text-soft);
  }
  .card__photo {
    position: absolute;
    inset: 0;
    background: radial-gradient(ellipse at 50% 50%, var(--photo-centre) 0%, var(--photo-mid) 45%, var(--card-black) 100%);
  }
  .brand {
    position: absolute;
    left: 0;
    right: 0;
    top: 276px;
    text-align: center;
    font-family: "Saira", sans-serif;
    font-weight: 700;
    font-size: 110px;
    line-height: 1;
    letter-spacing: 3px;
    color: var(--text-white);
    margin: 0;
  }
  .brand__rule {
    position: absolute;
    left: 342px;
    width: 516px;
    top: 429px;
    height: 1px;
    background: var(--accent-cyan);
    border: 0;
    margin: 0;
  }
  .tagline {
    position: absolute;
    left: 0;
    right: 0;
    top: 444px;
    text-align: center;
    font-size: 25px;
    font-weight: 400;
    color: var(--text-soft);
    margin: 0;
  }
  .dot {
    color: var(--accent-cyan);
  }
  .website {
    position: absolute;
    left: 0;
    right: 0;
    top: 600px;
    text-align: center;
    font-family: "Arimo", sans-serif;
    font-weight: 700;
    font-size: 37px;
    color: var(--text-white);
    margin: 0;
  }
  .address {
    position: absolute;
    left: 0;
    right: 0;
    top: 664px;
    text-align: center;
    font-size: 32px;
    font-weight: 400;
    color: var(--text-white);
    white-space: nowrap;
    margin: 0;
  }
</style>
</head>
<body>
  <main class="card">
    <div class="card__photo" role="img" aria-label="Blurred photo of nightclub lights in amber, blue and violet on black"></div>
    <h1 class="brand">Lumen</h1>
    <hr class="brand__rule">
    <p class="tagline">Restaurant <span class="dot">•</span> Nightclub</p>
    <p class="website">www.lumenstevenage.com</p>
    <p class="address">Lumen Stevenage Ltd <span class="dot">•</span> 42 Mill Lane <span class="dot">•</span> Stevenage <span class="dot">•</span> Herts <span class="dot">•</span> SG2 7PQ</p>
  </main>
</body>
</html>
```